Hot Pilates studio needs window graphics/ front signage

We need window graphics for the front of our hot pilates studio. We have several large front windows that are visible from the street and would be beneficial to have signage. Ember Loft offers several different heated classes on the mat including: Hot Pilates, Sculpt, Hot Barre. I would like for people that drive by to know what we are. The window dimensions are (4 windows) 41 inches X 61 inches, (4 windows) 34 inches X 61 inches (a total of 8 window panels)

Target Market(s)

fit women and men ages 16-65

Industry/Entity Type

fitness, pilates,

Font styles to use
Sans Serif

Colors

Designer to choose only greyscale colors for use in the design.

Requirements
Must have
• HOT PILATES
Nice to have
• our hashtag is #GlowOnMate

```html
<!DOCTYPE html>
<html lang="en">
<head>
<meta charset="utf-8">
<title>Ember Loft – Window Graphic</title>
<link href="https://fonts.googleapis.com/css2?family=Montserrat:wght@300;400;500;800&display=swap" rel="stylesheet">
<style>
  :root {
    --backdrop: #767474;
    --ink: #000000;
    --ink-soft: #444444;
    --paper: #ffffff;
    --photo-dark: #141414;
    --photo-mid: #2e2e2e;
  }
  * { margin: 0; padding: 0; box-sizing: border-box; }
  html, body {
    width: 1200px; height: 1200px; overflow: hidden;
    background: var(--backdrop);
    font-family: "Montserrat", Arial, sans-serif;
  }
  .window-panel {
    position: absolute; left: 323px; top: 100px;
    width: 561px; height: 1006px;
    background: var(--paper);
    overflow: hidden;
  }
  .hero-photo { position: absolute; inset: 0; width: 561px; height: 1006px; }
  .studio-name {
    position: absolute; top: 58px; left: 0; width: 100%;
    text-align: center; color: var(--paper);
    font-weight: 300; font-size: 58px; letter-spacing: 1px;
  }
  .class-badge {
    position: absolute; left: 142px; top: 175px;
    width: 278px; height: 278px; border-radius: 50%;
    background: var(--paper);
    display: flex; align-items: center; justify-content: center;
  }
  .class-badge::before {
    content: ""; position: absolute; inset: 7px;
    border: 1.5px solid var(--ink); border-radius: 50%;
  }
  .class-badge__text {
    text-align: center; color: var(--ink);
    font-size: 42px; line-height: 1.05; font-weight: 300;
  }
  .class-badge__text strong { font-weight: 800; }
  .call-to-action {
    position: absolute; top: 770px; left: 0; width: 100%;
    text-align: center; font-size: 50px; line-height: 1.08;
    color: var(--ink-soft); font-weight: 500;
  }
  .call-to-action strong { display: block; color: var(--ink); font-weight: 800; }
</style>
</head>
<body>
  <main class="window-panel">
    <svg class="hero-photo" viewBox="0 0 561 1006" role="img" aria-label="Greyscale photo of a woman exercising in a heated class">
      <defs>
        <linearGradient id="photoTone" x1="0" y1="0" x2="1" y2="1">
          <stop offset="0" stop-color="var(--photo-dark)"/>
          <stop offset="0.5" stop-color="var(--photo-mid)"/>
          <stop offset="1" stop-color="var(--photo-dark)"/>
        </linearGradient>
      </defs>
      <polygon points="0,0 561,0 561,750 0,564" fill="url(#photoTone)"/>
      <polygon points="0,520 561,560 561,750 0,564" fill="#ffffff" opacity="0.05"/>
    </svg>

    <h1 class="studio-name">Ember Loft</h1>

    <div class="class-badge">
      <p class="class-badge__text">HOT<br>PILATES<br><strong>&amp; MORE</strong></p>
    </div>

    <p class="call-to-action">WHAT ARE<br>YOU<strong>WAITING FOR?</strong></p>
  </main>
</body>
</html>
```